Bamboo Wash Cloth Package Design

We need packaging designed for Bamboo Washcloths the Package will be: 25 cm x 14 cm x 4 cm
I am attaching Pictures of the box and our logo. All the language that is on the box will need to be on there, but can be moved and customized.
In addition to our logo the front of the box should have on it:
7 100% Natural Bamboo Washcloths
1 for Every Day of the Week
Ultra Soft
7 Pack of 10" by 10" Washcloths
Free from Chemicals, Toxins and Dyes
Perfect for Sensitive and Delicate Skin
Generously Sized
All Natural Bamboo
The Back should have our logo and the following language:
The Willow Nest Collection's premium 100% natural bamboo washcloths are the softest most gentle washcloths available. They are perfect for babies' delicate skin and for adults.
Willow Nest only uses the highest quality bamboo on the planet. Our perfectly sized washcloths are carefully woven into plush goodness featuring maximum absorbency and durability.
These eco-friendly washcloths, created from a sustainable source, are naturally antibacterial, hypoallergenic, and free from all dyes, chemicals, and toxins. They are comfort guaranteed and will leave you and your baby's skin feeling as pristine as nature intended.
The icons on the bottom of the box should also be used.
Additional thoughts:
1. Would like to see Bamboo and a Baby Panda worked into the design.
2.The Box can be 4 color.
3. I am attaching 3 box Pictures. The first 2 are picture of what our box is like for reference.
4. the 3rd is an idea of the color scheme I'd like to see utilized.
Please let me know if you have any questions.
Target Market(s)
Mothers and people who are environmentally conscious
Look and feel

```html
<!DOCTYPE html>
<html lang="en">
<head>
<meta charset="utf-8">
<title>Willow Nest – Bamboo Washcloth Box Dieline</title>
<link href="https://fonts.googleapis.com/css2?family=Arimo:wght@400;700&family=Varela+Round&family=Cutive+Mono&family=Open+Sans:wght@400&display=swap" rel="stylesheet">
<style>
  :root {
    --kraft: #c49a6c;
    --kraft-deep: #b88b5a;
    --orange: #fbb040;
    --orange-deep: #f7941d;
    --green: #0b8a3e;
    --yellow: #f5d90a;
    --red: #e8262b;
    --white: #ffffff;
    --page: #ffffff;
  }
  * { box-sizing: border-box; margin: 0; padding: 0; }
  html, body { width: 1200px; height: 1200px; overflow: hidden; background: var(--page); }
  .canvas { position: relative; width: 1200px; height: 1200px; }

  .panel { position: absolute; background: var(--kraft); overflow: hidden; }
  .front { left: 312px; top: 166px; width: 578px; height: 337px; }
  .back  { left: 312px; top: 567px; width: 578px; height: 338px; }
  .side  { width: 97px; height: 338px; }
  .side-right { left: 959px; top: 166px; }
  .side-left  { left: 158px; top: 567px; }

  /* week rail */
  .week-rail { position: absolute; left: 0; top: 38px; width: 578px; height: 20px; background: var(--orange); border-radius: 10px; }
  .cloth { position: absolute; top: 22px; width: 54px; height: 54px; background: var(--white); border-radius: 7px; box-shadow: inset 0 0 6px rgba(0,0,0,.08); }
  .day { position: absolute; top: 83px; width: 80px; text-align: center; font: 17px 'Cutive Mono', monospace; color: var(--white); letter-spacing: 1px; }
  .day.sunday { color: var(--red); }

  /* pack badge */
  .pack-badge { position: absolute; left: 0; top: 139px; width: 90px; height: 57px; background: var(--green); border: 3px dashed var(--yellow); border-left: none; border-radius: 0 6px 6px 0; padding: 9px 0 0 11px; font: 12.5px/16px 'Open Sans', sans-serif; color: var(--orange); }

  /* title label */
  .title-frame { position: absolute; left: 121px; top: 113px; width: 312px; height: 164px; border: 2px solid var(--white); border-radius: 20px; }
  .title-frame::after { content: ""; position: absolute; inset: 4px; border: 1.5px solid var(--white); border-radius: 16px; }
  .title-card { position: absolute; left: 150px; top: 124px; width: 270px; height: 142px; background: var(--white); border-radius: 10px; }
  .bamboo-stalk { position: absolute; left: 138px; top: 112px; width: 34px; height: 166px; background: linear-gradient(90deg, var(--kraft) 0 20%, #e9d7c2 20% 80%, var(--kraft) 80%); opacity: .7; }
  .title-line { position: absolute; right: 198px; font-family: 'Varela Round', sans-serif; white-space: nowrap; }
  .title-natural { top: 146px; font-size: 27px; color: var(--kraft-deep); }
  .title-bamboo { top: 180px; font-size: 31px; color: var(--kraft-deep); }
  .title-washcloths { top: 213px; font: 700 37px 'Arimo', sans-serif; color: var(--orange-deep); }

  .soft-badge { position: absolute; left: 466px; top: 142px; width: 96px; height: 96px; }

  .feature { position: absolute; font: 10.5px/15px 'Open Sans', sans-serif; color: var(--orange); white-space: nowrap; }

  /* side panels */
  .side-label { position: absolute; left: 10px; top: 10px; width: 68px; height: 318px; background: var(--white); }
  .side-name { position: absolute; left: 44px; top: 169px; transform: translate(-50%, -50%) rotate(-90deg); font: 700 47px 'Arimo', sans-serif; color: var(--kraft); white-space: nowrap; }

  /* back */
  .brand-card { position: absolute; left: 14px; top: 21px; width: 126px; height: 290px; background: var(--white); }
  .brand-name { position: absolute; left: 5px; top: 12px; font: 700 29px/31px 'Arimo', sans-serif; color: var(--kraft); }
  .bamboo-grove { position: absolute; left: 8px; top: 104px; width: 110px; height: 180px; background: linear-gradient(180deg, #f4ebe0, #e6d3bd); }
  .copy { position: absolute; left: 166px; font: 9.6px/12.4px 'Arimo', sans-serif; color: var(--white); white-space: nowrap; }
  .care { position: absolute; left: 234px; top: 247px; font: 9.4px/12px 'Cutive Mono', monospace; color: var(--white); white-space: nowrap; }
  .care-icons { position: absolute; left: 284px; top: 310px; width: 146px; height: 20px; }
</style>
</head>
<body>
<div class="canvas">

  <section class="panel front" aria-label="Front panel">
    <div class="week-rail"></div>
    <div class="cloth" style="left:21px"></div>
    <div class="cloth" style="left:101px"></div>
    <div class="cloth" style="left:181px"></div>
    <div class="cloth" style="left:262px"></div>
    <div class="cloth" style="left:342px"></div>
    <div class="cloth" style="left:422px"></div>
    <div class="cloth" style="left:503px"></div>
    <span class="day sunday" style="left:8px">SUN</span>
    <span class="day" style="left:88px">MON</span>
    <span class="day" style="left:168px">TUE</span>
    <span class="day" style="left:249px">WED</span>
    <span class="day" style="left:329px">THE</span>
    <span class="day" style="left:409px">FRI</span>
    <span class="day" style="left:490px">SAT</span>

    <div class="pack-badge">PACK OF<br>10″BY10″</div>

    <div class="title-frame"></div>
    <div class="title-card"></div>
    <div class="bamboo-stalk" role="img" aria-label="Line drawing of a bamboo stalk with leaves"></div>
    <span class="title-line title-natural">100% natural</span>
    <span class="title-line title-bamboo">bamboo</span>
    <span class="title-line title-washcloths">washcloths</span>

    <svg class="soft-badge" viewBox="0 0 96 96">
      <polygon fill="var(--orange)" points="48,2 56,20 72,8 72,28 92,26 80,42 94,56 74,60 80,80 62,74 56,94 48,78 40,94 34,74 16,80 22,60 2,56 16,42 4,26 24,28 24,8 40,20"/>
      <circle cx="48" cy="48" r="30" fill="var(--green)"/>
      <text x="48" y="44" text-anchor="middle" font-family="Varela Round, sans-serif" font-size="15" fill="var(--orange)">ultra</text>
      <text x="48" y="61" text-anchor="middle" font-family="Varela Round, sans-serif" font-size="15" fill="var(--orange)">soft</text>
    </svg>

    <p class="feature" style="left:22px;top:294px">free from chemical<br>toxins and dyes</p>
    <p class="feature" style="left:167px;top:294px">perfect for sensitive<br>and delicate skin</p>
    <p class="feature" style="left:322px;top:302px">generously sized</p>
    <p class="feature" style="left:452px;top:302px">all natural bamboo</p>
  </section>

  <section class="panel side side-right" aria-label="Right side panel">
    <div class="side-label"></div>
    <span class="side-name">willow nest</span>
  </section>

  <section class="panel side side-left" aria-label="Left side panel">
    <div class="side-label"></div>
    <span class="side-name">willow nest</span>
  </section>

  <section class="panel back" aria-label="Back panel">
    <div class="brand-card">
      <p class="brand-name">willow<br>nest</p>
      <div class="bamboo-grove" role="img" aria-label="Line drawing of a bamboo grove"></div>
    </div>

    <p class="copy" style="top:57px">The Willow Nest Collection's premium 100% naturalbamboo washcloths are the sofest<br>most gentle washcloths available. They are perfect for babies' delicate skin and for adults</p>
    <p class="copy" style="top:107px">Willow Nest only uses the highest quality bamboo on the planet. Our perfectly sized wash<br>cloths are carefully woven into plush goodness featuring maximum absorbency and durability</p>
    <p class="copy" style="top:152px;left:164px">These eco-friendly waashcloths, created from a sustainable source, are naturallyantibacterial,<br>hypoallergenic, and free from all dyes,chemicals,and toxins. They are comfort guaranteed and<br>will leave you and your baby's skin feeling as pristine as nature intended</p>

    <p class="care">Care Instruction : wash before use.<br>Machine Wash cold with like colors. Do not<br>use bleach. Tumble dry low. no not iron.<br>Made in china</p>

    <svg class="care-icons" viewBox="0 0 146 20" fill="none" stroke="var(--white)" stroke-width="1">
      <path d="M2 5 L5 17 H23 L26 5 M2 5 Q7 2 10 5 Q14 8 18 5 Q22 2 26 5"/>
      <text x="14" y="15" text-anchor="middle" font-size="6" fill="var(--white)" stroke="none" font-family="Arimo, sans-serif">30</text>
      <path d="M38 17 L50 3 L62 17 Z M40 3 L60 18 M60 3 L40 18"/>
      <rect x="80" y="3" width="15" height="15"/><circle cx="87.5" cy="10.5" r="5.5"/><path d="M80 3 L95 18 M95 3 L80 18"/>
      <path d="M113 15 H139 L136 8 H119 Q114 8 113 15 Z M112 4 L140 18 M140 4 L112 18"/>
    </svg>
  </section>

</div>
</body>
</html>
```